BRIGHTWAVE PARTNERS NAMECARD

Need to design a name card with an existing logo.

As we are professional corporate services provider our name card has to project a professional image.
Should be corporate, simple & professional.

Our corporate color is maroon red but not too dull.

Please refer to our website at www.brightwavepartners.com.sg

Would attach our logo herewith.

Front surface of namecard details:
BRIGHTWAVE PARTNERS PTE LTD
Registration No. 208731945K

Lowe Hui Ting CA (Singapore)
Director

Tel +65 6481 2957
Mobile +65 9172 3806
lowe@brightwavepartners.com.sg
www.brightwavepartners.com.sg

47 Palmer Lane
#07-14 Harbourlight Plaza
Singapore 274153

Back of namecard:-
OUR CORE SERVICES
Incorporation services
Corporate Secretarial Services
Accountancy service
Goods & Services Taxation
Corporate & Personal Taxation
Financial Reporting
Payroll Administration

AFFILIATES:
TRIVANTA CORPORATE SERVICES PTE LTD
BRIGHTWAVEREGISTRYPTE LTD
ORR MANAGEMENT SERVICES PTE LTD
DW LIM AND COMPANY PTE LTD
LEDGERWISE ACADEMY

```html
<!DOCTYPE html>
<html lang="en">
<head>
<meta charset="utf-8">
<title>Brightwave Partners Namecard</title>
<link href="https://fonts.googleapis.com/css2?family=Source+Sans+3:wght@400;600;700&display=swap" rel="stylesheet">
<style>
  :root {
    --backdrop: #e4e2df;
    --card: #151515;
    --card-edge: #262626;
    --maroon: #cf2236;
    --silver: #b8b8b8;
    --white: #f2f2f2;
    --rule: #6a6a6a;
  }
  * { box-sizing: border-box; margin: 0; padding: 0; }
  html, body {
    width: 1200px; height: 864px; overflow: hidden;
    background: var(--backdrop);
    font-family: "Source Sans 3", Arial, sans-serif;
  }
  .stage {
    width: 1200px; height: 864px;
    display: flex; align-items: center; justify-content: center; gap: 44px;
  }
  .card {
    width: 540px; height: 310px;
    background: var(--card);
    border: 1px solid var(--card-edge);
    position: relative;
    color: var(--white);
  }

  /* Back */
  .card-back {
    display: flex; flex-direction: column; align-items: center;
    padding-top: 30px; text-align: center;
  }
  .back-name {
    color: var(--silver); font-weight: 600; font-size: 30px;
    letter-spacing: 1px; line-height: 1;
  }
  .back-rule {
    width: 300px; height: 1px; margin: 14px 0 8px;
    background: linear-gradient(90deg, transparent, var(--rule), transparent);
  }
  .back-heading { color: var(--maroon); font-size: 13px; margin-bottom: 4px; }
  .back-list { color: var(--silver); font-size: 12.5px; line-height: 1.45; }
  .back-list .dot { color: var(--maroon); padding: 0 3px; }

  /* Front */
  .card-front { display: flex; align-items: center; }
  .front-name {
    width: 262px; padding-left: 34px;
    color: var(--maroon); font-weight: 600; font-size: 34px;
    line-height: 0.95; letter-spacing: 0.5px;
  }
  .front-divider {
    width: 1px; height: 230px;
    background: linear-gradient(180deg, transparent, #d9d9d9 30%, #d9d9d9 70%, transparent);
  }
  .front-details { padding-left: 22px; font-size: 13px; line-height: 1.35; }
  .person { color: var(--maroon); font-weight: 700; font-size: 16px; }
  .role { margin-bottom: 10px; }
  .company { color: var(--maroon); font-weight: 700; }
  .address { margin-bottom: 8px; }
  .contact { display: flex; align-items: center; gap: 7px; }
  .contact svg { width: 11px; height: 11px; fill: var(--maroon); flex: none; }
  .registration { margin-top: 2px; }
</style>
</head>
<body>
<main class="stage">

  <section class="card card-back">
    <div class="back-name">BRIGHTWAVE PARTNERS</div>
    <div class="back-rule"></div>
    <div class="back-heading">Our Core Services</div>
    <div class="back-list">
      Incorporation services<span class="dot">•</span>Corporate Secretarial Services<br>
      Accountancy service<span class="dot">•</span>Goods &amp; Services Taxation<br>
      Corporate &amp; Personal Taxation<span class="dot">•</span>Financial Reporting<br>
      <span class="dot">•</span>Payroll Administration
    </div>
    <div class="back-rule"></div>
    <div class="back-heading">Affiliates</div>
    <div class="back-list">
      Trivanta Corporate Services PTE LTD<span class="dot">•</span>Brightwaveregistry PTE LTD<br>
      Orr Management Services PTE LTD<span class="dot">•</span>DW Lim and<br>
      company PTE LTD<span class="dot">•</span>Ledgerwise Academy
    </div>
    <div class="back-rule"></div>
  </section>

  <section class="card card-front">
    <div class="front-name">BRIGHTWAVE<br>PARTNERS</div>
    <div class="front-divider"></div>
    <div class="front-details">
      <div class="person">Lowe Hui Ting CA</div>
      <div class="role">Director</div>
      <div class="company">Brightwave Partners PTE LTD</div>
      <div class="address">47 Palmer Lane<br>#07-14 Harbourlight Plaza<br>Singapore 274153</div>
      <div class="contact">
        <svg viewBox="0 0 12 12" aria-hidden="true"><path d="M2 1h2.5l1 2.5-1.3 1a6 6 0 0 0 3.3 3.3l1-1.3L11 7.5V10a1 1 0 0 1-1 1A9 9 0 0 1 1 2a1 1 0 0 1 1-1z"/></svg>
        +65 6481 2957
      </div>
      <div class="contact">
        <svg viewBox="0 0 12 12" aria-hidden="true"><path d="M3.5 0h5a1 1 0 0 1 1 1v10a1 1 0 0 1-1 1h-5a1 1 0 0 1-1-1V1a1 1 0 0 1 1-1zm.5 1.5v8h4v-8z"/></svg>
        +65 9172 3806
      </div>
      <div class="contact">
        <svg viewBox="0 0 12 12" aria-hidden="true"><path d="M0 2.5h12v7H0zm1 1v.4l5 3 5-3v-.4z"/></svg>
        lowe@brightwavepartners.com.sg
      </div>
      <div class="contact">
        <svg viewBox="0 0 12 12" aria-hidden="true"><circle cx="6" cy="6" r="5.5"/><path d="M1 6h10M6 .5c-2 2.5-2 8.5 0 11M6 .5c2 2.5 2 8.5 0 11" stroke="#151515" stroke-width="0.9" fill="none"/></svg>
        www.brightwavepartners.com.sg
      </div>
      <div class="registration">Registration No. 208731945K</div>
    </div>
  </section>

</main>
</body>
</html>
```